Rent Kiosks and Tablets

Website for rental kiosks and tablets following the model / style http://www.velquorin.com/. May be the same, with changes in visual identity.
The site should also have an online order system like an e-commerce, which allows payment by credit card and ticket.

The company is called Pombruxa.com and feel free to create/suggest styles of names design.

Target Market(s)

Events, trade shows, marketing companies.

Industry/Entity Type

Credit Card

Font styles to use
Sans Serif

Colors

Designer to choose colors to be used in the design.

```html
<!DOCTYPE html>
<html lang="en">
<head>
<meta charset="utf-8">
<title>Pombruxa.com – Rent Kiosks and Tablets</title>
<link rel="stylesheet" href="https://fonts.googleapis.com/css2?family=Mulish:wght@300;400;600;700&family=Libre+Baskerville:wght@700&display=swap">
<style>
:root{
  --accent:#e0533c;
  --accent-dark:#c8432d;
  --ink:#222;
  --muted:#666;
  --topbar:#151515;
  --nav:#1f1f1f;
  --light:#ededed;
  --dark:#2e2e2e;
  --footer:#1a1a1a;
  --white:#fff;
}
*{margin:0;padding:0;box-sizing:border-box}
html,body{width:1200px;height:3097px;overflow:hidden}
body{font-family:"Mulish",Arial,sans-serif;color:var(--ink);background:var(--white);position:relative}
.abs{position:absolute}
.topbar{left:0;top:0;width:1200px;height:52px;background:var(--topbar);color:#aaa;font-size:12px}
.topbar span{position:absolute;top:19px}
.topbar .sep{position:absolute;top:0;width:1px;height:52px;background:#333}
.navbar{left:0;top:52px;width:1200px;height:72px;background:var(--nav)}
.brand{left:152px;top:72px;font-size:28px;font-weight:700;color:var(--accent)}
.menu{right:155px;top:78px;display:flex;gap:34px;font-size:14px;color:#ddd}
.hero{left:0;top:124px;width:1200px;height:444px;background:linear-gradient(100deg,#4a2e1e 0%,#8a5a3a 30%,#c08a5a 55%,#6b4630 80%,#3c2618 100%)}
.hero-device{left:645px;top:40px;width:490px;height:390px;border-radius:10px;background:linear-gradient(180deg,#3a3a3a,#cfcfcf)}
.hero-title{left:186px;top:165px;color:var(--white);font-size:36px;font-weight:700;line-height:44px}
.arrow{width:58px;height:58px;border-radius:50%;background:rgba(255,255,255,.85)}
.arrow svg{display:block;margin:17px auto}
h2.section-title{position:absolute;left:0;width:1200px;text-align:center;font-weight:400;font-size:37px;color:#222}
h2 em{font-style:normal;color:var(--accent)}
.lead{left:250px;width:700px;text-align:center;font-size:12px;line-height:20px;color:var(--muted)}
.rule{left:70px;top:678px;width:1060px;height:1px;background:#e3e3e3}
.video{left:165px;top:820px;width:434px;height:297px;background:#dcdcdc}
.video .play{position:absolute;left:180px;top:108px;width:76px;height:52px;border-radius:12px;background:#1a1a1a}
.video .bar{position:absolute;left:0;bottom:0;width:434px;height:34px;background:#1b1b1b}
.video .progress{position:absolute;left:0;bottom:30px;width:434px;height:5px;background:#555}
.video .progress i{display:block;width:90px;height:5px;background:#d32b1f}
.checks{left:627px;top:826px;list-style:none}
.checks li{display:flex;align-items:center;gap:16px;height:49px;font-size:13px;color:#444}
.checks .box{width:24px;height:24px;border:2px solid var(--accent);border-radius:3px;display:flex;align-items:center;justify-content:center}
.btn{display:flex;align-items:center;justify-content:center;background:var(--accent);color:var(--white);font-size:13px;font-weight:600;letter-spacing:.5px;border-radius:4px;box-shadow:0 2px 0 var(--accent-dark)}
.compat{left:0;top:1180px;width:1200px;height:296px;background:var(--light)}
.platform{display:flex;align-items:center;justify-content:center;flex-direction:column;gap:8px;font-size:18px;font-weight:600;color:#333}
.platform .mark{width:60px;height:60px;border-radius:6px}
.leverage{left:0;top:1476px;width:1200px;height:335px;background:var(--dark)}
.lev-title{left:152px;top:1538px;color:var(--white);font-size:34px;font-weight:400;line-height:42px}
.lev-text{left:152px;top:1628px;width:420px;color:#8a8a8a;font-size:13px;line-height:20px}
.tablets{left:671px;top:1522px;width:464px;height:258px;border-radius:12px;background:linear-gradient(160deg,#555 0%,#bdbdbd 60%,#ededed 100%)}
.cons-title{left:152px;top:1905px;font-size:34px;font-weight:400;line-height:40px}
.cons-text{left:152px;top:1998px;width:470px;font-size:13.5px;line-height:20px;color:#333}
.hex{width:108px;height:122px}
.hex text{font-family:"Mulish",Arial,sans-serif}
.trusted{left:0;top:2224px;width:1200px;height:240px;background:var(--light)}
.press{left:150px;top:2322px;width:900px;display:flex;justify-content:space-between;align-items:center;color:#222}
.press span{font-family:"Libre Baskerville",Georgia,serif;font-size:19px}
.blog-item{width:300px;display:flex;gap:16px}
.blog-thumb{width:129px;height:129px;flex:none;background:linear-gradient(160deg,#7a3a2a,#2b2b2b 55%,#d8d8d8)}
.blog-item h3{font-size:15px;font-weight:600;line-height:19px;color:#222}
.blog-item p{font-size:11.5px;line-height:17px;color:#888;margin-top:10px}
.footer{left:0;top:3032px;width:1200px;height:65px;background:var(--footer)}
.foot-links{left:152px;top:3056px;display:flex;gap:20px;font-size:12px;color:#bbb;letter-spacing:.5px}
.social{top:3051px;width:24px;height:24px;border-radius:50%;background:var(--accent)}
</style>
</head>
<body>

<header>
  <div class="abs topbar">
    <svg class="abs" style="left:152px;top:20px" width="16" height="12" viewBox="0 0 16 12"><rect x="1" y="1" width="14" height="10" fill="none" stroke="#999"/><path d="M1 1l7 6 7-6" fill="none" stroke="#999"/></svg>
    <span style="left:174px">rentals@pombruxa.com</span>
    <svg class="abs" style="left:330px;top:18px" width="14" height="14" viewBox="0 0 14 14"><path d="M3 1l3 3-2 2c1 2 2 3 4 4l2-2 3 3-2 2C6 13 1 8 1 3z" fill="#999"/></svg>
    <span style="left:352px">+00 555 013 270</span>
    <div class="sep" style="left:638px"></div>
    <svg class="abs" style="left:652px;top:19px" width="14" height="14" viewBox="0 0 14 14"><circle cx="6" cy="6" r="4.5" fill="none" stroke="#999" stroke-width="1.5"/><path d="M9.5 9.5l3.5 3.5" stroke="#999" stroke-width="1.5"/></svg>
    <span style="left:676px">Enter your keywords</span>
    <div class="sep" style="left:820px"></div>
    <svg class="abs" style="left:834px;top:18px" width="16" height="15" viewBox="0 0 16 15"><path d="M1 1h3l2 9h8l1-6H5" fill="none" stroke="#999" stroke-width="1.4"/><circle cx="7" cy="13" r="1.3" fill="#999"/><circle cx="13" cy="13" r="1.3" fill="#999"/></svg>
    <span style="left:858px">Shopping Cart <b style="color:var(--accent)">03 items</b> for <b style="color:var(--accent)">$12.560</b></span>
  </div>
  <div class="abs navbar"></div>
  <div class="abs brand">Pombruxa.com</div>
  <nav class="abs menu">
    <span>Services</span><span>Products</span><span>Leasing</span><span>Case Studies ▾</span><span>Company ▾</span>
  </nav>
</header>

<section class="abs hero">
  <div class="abs hero-device" role="img" aria-label="Countertop tablet kiosk with cup dispenser in a blurred café setting"></div>
  <h1 class="abs hero-title">All-in-One Solutions<br>for Your Business</h1>
  <div class="abs arrow" style="left:92px;top:190px"><svg width="24" height="24" viewBox="0 0 24 24"><path d="M15 4l-8 8 8 8" fill="none" stroke="#444" stroke-width="4"/></svg></div>
  <div class="abs arrow" style="left:1044px;top:190px"><svg width="24" height="24" viewBox="0 0 24 24"><path d="M9 4l8 8-8 8" fill="none" stroke="#444" stroke-width="4"/></svg></div>
</section>

<section class="solutions">
  <h2 class="section-title" style="top:612px">We Provide <em>Web</em> Solutions</h2>
  <div class="abs rule"></div>
  <p class="abs lead" style="top:706px">Lorem ipsum dolor sit amet, consectetur adipiscing elit. Aliquam laoreet sodales lacinia. Curabitur ut purus tincidunt, iaculis elit a, eleifend augue. Phasellus blandit augue vel sollicitudin blandit.</p>
  <div class="abs video" role="img" aria-label="Embedded product video">
    <div class="play"><svg style="display:block;margin:14px auto" width="22" height="24" viewBox="0 0 22 24"><path d="M2 1l19 11-19 11z" fill="#fff"/></svg></div>
    <div class="progress"><i></i></div>
    <div class="bar"></div>
  </div>
  <ul class="abs checks">
    <li><span class="box"><svg width="14" height="12" viewBox="0 0 14 12"><path d="M1 6l4 4 8-9" fill="none" stroke="#e0533c" stroke-width="2.5"/></svg></span>Aenean sollicitudin, lorem quis bibendum auctor nisi elit</li>
    <li><span class="box"><svg width="14" height="12" viewBox="0 0 14 12"><path d="M1 6l4 4 8-9" fill="none" stroke="#e0533c" stroke-width="2.5"/></svg></span>Consequat ipsum, nec sagittis sem nibh id elit</li>
    <li><span class="box"><svg width="14" height="12" viewBox="0 0 14 12"><path d="M1 6l4 4 8-9" fill="none" stroke="#e0533c" stroke-width="2.5"/></svg></span>Duis sed odio sit amet nibh vulputate cursus</li>
    <li><span class="box"><svg width="14" height="12" viewBox="0 0 14 12"><path d="M1 6l4 4 8-9" fill="none" stroke="#e0533c" stroke-width="2.5"/></svg></span>Morbi accumsan ipsum velit</li>
    <li><span class="box"><svg width="14" height="12" viewBox="0 0 14 12"><path d="M1 6l4 4 8-9" fill="none" stroke="#e0533c" stroke-width="2.5"/></svg></span>Lorem quis bibendum auctor nisi elit</li>
  </ul>
  <div class="abs btn" style="left:627px;top:1079px;width:134px;height:41px">READ MORE</div>
</section>

<section class="abs compat">
  <h2 class="section-title" style="top:32px">Campatible with:</h2>
  <div class="abs platform" style="left:380px;top:112px;width:110px"><span class="mark" style="background:#1c8fd6"></span>Quadrix</div>
  <div class="abs platform" style="left:570px;top:112px;width:110px"><span class="mark" style="background:#6a8fb8"></span>Orchard</div>
  <div class="abs platform" style="left:740px;top:112px;width:140px"><span class="mark" style="background:#8fc43f;border-radius:50%"></span>Greenbot</div>
</section>

<section class="abs leverage"></section>
<h2 class="abs lev-title">Leverage tablets for<br>your business</h2>
<p class="abs lev-text">We provide solutions for almost any tablet on the market, offering a wide variety of options to meet your project needs.</p>
<div class="abs btn" style="left:152px;top:1703px;width:134px;height:43px">READ MORE</div>
<div class="abs tablets" role="img" aria-label="Tablet kiosk stands with mounted tablets"></div>

<section class="consulting">
  <h2 class="abs cons-title">Consulting you<br>in the right direction.</h2>
  <p class="abs cons-text">As pioneers of integrating tablet computers into the business landscape, we strive to share our knowledge with every client to ensure you have a successful tablet kiosk deployment. Providing solutions for every industry, we are familiar with your unique integration requirements.</p>
  <div class="abs btn" style="left:152px;top:2123px;width:134px;height:42px">READ MORE</div>

  <svg class="abs hex" style="left:658px;top:1893px" viewBox="0 0 108 122"><polygon points="54,0 108,30 108,92 54,122 0,92 0,30" fill="#e0533c"/><path d="M38 50l16-8 16 8-16 8z M44 54v8c6 4 14 4 20 0v-8" fill="#fff"/><text x="54" y="86" text-anchor="middle" fill="#fff" font-size="11" font-weight="700">EDUCATION</text></svg>
  <svg class="abs hex" style="left:798px;top:1893px" viewBox="0 0 108 122"><polygon points="54,0 108,30 108,92 54,122 0,92 0,30" fill="#e0533c"/><rect x="44" y="36" width="20" height="30" rx="3" fill="none" stroke="#fff" stroke-width="3"/><text x="54" y="86" text-anchor="middle" fill="#fff" font-size="11" font-weight="700">POS</text></svg>
  <svg class="abs hex" style="left:938px;top:1893px" viewBox="0 0 108 122"><polygon points="54,0 108,30 108,92 54,122 0,92 0,30" fill="#e0533c"/><circle cx="54" cy="52" r="14" fill="none" stroke="#fff" stroke-width="3"/><path d="M36 40v24M72 40v24" stroke="#fff" stroke-width="3"/><text x="54" y="86" text-anchor="middle" fill="#fff" font-size="11" font-weight="700">RESTAURANT</text></svg>
  <svg class="abs hex" style="left:658px;top:2035px" viewBox="0 0 108 122"><polygon points="54,0 108,30 108,92 54,122 0,92 0,30" fill="#e0533c"/><rect x="40" y="40" width="28" height="24" rx="3" fill="#fff"/><path d="M54 45v14M47 52h14" stroke="#e0533c" stroke-width="4"/><text x="54" y="86" text-anchor="middle" fill="#fff" font-size="11" font-weight="700">MEDICAL</text></svg>
  <svg class="abs hex" style="left:798px;top:2035px" viewBox="0 0 108 122"><polygon points="54,0 108,30 108,92 54,122 0,92 0,30" fill="#e0533c"/><path d="M38 40h6l4 16h16l3-11H46" fill="none" stroke="#fff" stroke-width="3"/><circle cx="50" cy="63" r="2.5" fill="#fff"/><circle cx="62" cy="63" r="2.5" fill="#fff"/><text x="54" y="86" text-anchor="middle" fill="#fff" font-size="11" font-weight="700">RETAIL</text></svg>
  <svg class="abs hex" style="left:938px;top:2035px" viewBox="0 0 108 122"><polygon points="54,0 108,30 108,92 54,122 0,92 0,30" fill="#e0533c"/><circle cx="54" cy="50" r="12" fill="none" stroke="#fff" stroke-width="3"/><path d="M62 58l8 8" stroke="#fff" stroke-width="3"/><text x="54" y="86" text-anchor="middle" fill="#fff" font-size="11" font-weight="700">NON-PROFIT</text></svg>
</section>

<section class="abs trusted">
  <h2 class="section-title" style="top:28px">They trusted Us</h2>
</section>
<div class="abs press">
  <span style="font-style:italic">Venturist</span>
  <span>The Halden Ledger</span>
  <span style="display:flex;align-items:center;gap:6px"><i style="display:inline-block;width:20px;height:20px;border-radius:50%;background:#222"></i>bytnet</span>
  <span>Booth Market</span>
  <span>QUICKFIRM</span>
  <span style="font-size:15px">Bayline Courier</span>
</div>

<section class="blog">
  <h2 class="section-title" style="top:2498px">Blog News</h2>
  <p class="abs lead" style="top:2548px">Lorem ipsum dolor sit amet, consectetur adipiscing elit. Aliquam laoreet sodales lacinia. Curabitur ut purus tincidunt, iaculis elit a, eleifend augue. Phasellus blandit augue vel sollicitudin blandit.</p>

  <article class="abs blog-item" style="left:152px;top:2658px"><div class="blog-thumb" role="img" aria-label="Blog post photo of a tablet kiosk"></div><div><h3>Nullam nunc purus, pretium sed faucibus nec.</h3><p>Nunc purus orci, adipiscig non ipsum non, pellentesque fringilla sapien.</p></div></article>
  <article class="abs blog-item" style="left:462px;top:2658px"><div class="blog-thumb" role="img" aria-label="Blog post photo of a tablet kiosk"></div><div><h3>Nullam nunc purus, pretium sed faucibus nec.</h3><p>Nunc purus orci, adipiscig non ipsum non, pellentesque fringilla sapien.</p></div></article>
  <article class="abs blog-item" style="left:764px;top:2658px"><div class="blog-thumb" role="img" aria-label="Blog post photo of a tablet kiosk"></div><div><h3>Nullam nunc purus, pretium sed faucibus nec.</h3><p>Nunc purus orci, adipiscig non ipsum non, pellentesque fringilla sapien.</p></div></article>
  <article class="abs blog-item" style="left:152px;top:2825px"><div class="blog-thumb" role="img" aria-label="Blog post photo of a tablet kiosk"></div><div><h3>Nullam nunc purus, pretium sed faucibus nec.</h3><p>Nunc purus orci, adipiscig non ipsum non, pellentesque fringilla sapien.</p></div></article>
  <article class="abs blog-item" style="left:462px;top:2825px"><div class="blog-thumb" role="img" aria-label="Blog post photo of a tablet kiosk"></div><div><h3>Nullam nunc purus, pretium sed faucibus nec.</h3><p>Nunc purus orci, adipiscig non ipsum non, pellentesque fringilla sapien.</p></div></article>
  <article class="abs blog-item" style="left:764px;top:2825px"><div class="blog-thumb" role="img" aria-label="Blog post photo of a tablet kiosk"></div><div><h3>Nullam nunc purus, pretium sed faucibus nec.</h3><p>Nunc purus orci, adipiscig non ipsum non, pellentesque fringilla sapien.</p></div></article>
</section>

<footer>
  <div class="abs footer"></div>
  <nav class="abs foot-links"><span>SERVICES</span><span>PRODUCTS</span><span>LEASING</span><span>COMPANY</span><span>CASE STUDIES</span><span>SITEMAP</span></nav>
  <span class="abs social" style="left:944px"></span>
  <span class="abs social" style="left:974px"></span>
  <span class="abs social" style="left:1004px"></span>
</footer>

</body>
</html>
```